Crestline Lending Group Business Cards

We are looking to revamp the current business cards each of our locations uses. We are a lending company that specializes in personal loans, title loans, and tax services. We have locations in New Mexico, Texas, and Oklahoma.

We would like a cleaner, sleeker look while still highlighting what we offer. Title Loans, Personal Loans & Tax Services. We also want to include our referral fee somewhere on the card. We would like to see an English option as well as a Spanish option for the cards.

PLEASE NOTE: Some business cards do not include the employee's name but just the store's location, while others will include both.

These are double-sided business cards, and we would like to see proof if possible. I have included proofs of our current business cards for you to review below, as well as our company logo. Feel free to get creative with the logo, etc! Colors should match the logo; however, you do not need to use all of our logo colors if you don't want to.

```html
<!DOCTYPE html>
<html lang="en">
<head>
<meta charset="utf-8">
<title>Crestline Lending Group Business Cards</title>
<link rel="stylesheet" href="https://fonts.googleapis.com/css2?family=Montserrat:wght@400;500;600;700;800&display=swap">
<style>
  :root {
    --backdrop: #e6e5e1;
    --brand-green: #0f4d2b;
    --brand-red: #b5161e;
    --paper: #f7f6f3;
    --ink: #1e1e1e;
    --white: #ffffff;
  }
  * { margin: 0; padding: 0; box-sizing: border-box; }
  html, body {
    width: 1200px;
    height: 765px;
    overflow: hidden;
    background: var(--backdrop);
    font-family: "Montserrat", sans-serif;
  }
  .canvas { position: relative; width: 1200px; height: 765px; }

  .card { position: absolute; width: 417px; height: 238px; }

  /* Front side */
  .card-front {
    left: 285px; top: 129px;
    background: var(--brand-green);
    color: var(--white);
    text-align: center;
  }
  .front-name {
    position: absolute; left: 0; right: 0; top: 92px;
    font-size: 25px; font-weight: 600; letter-spacing: -0.2px;
    color: var(--white);
  }
  .front-web {
    position: absolute; left: 0; right: 0; top: 152px;
    font-size: 12px; font-weight: 700; color: var(--brand-red);
  }
  .front-services {
    position: absolute; left: 0; right: 0; top: 198px;
    font-size: 11px; font-weight: 500; letter-spacing: 0.2px;
  }

  /* Back side */
  .card-back {
    left: 499px; top: 398px;
    background: var(--paper);
  }
  .referral {
    position: absolute; left: 18px; width: 128px; top: 33px;
    text-align: center; color: var(--brand-green); line-height: 1.1;
  }
  .referral-title { font-size: 12px; font-weight: 800; }
  .referral-sub { font-size: 11px; font-weight: 500; }
  .referral-amount { font-size: 26px; font-weight: 800; color: var(--brand-red); margin-top: 2px; }

  .back-mark {
    position: absolute; left: 18px; width: 128px; top: 118px;
    text-align: center; color: var(--brand-green);
    font-size: 21px; font-weight: 700; line-height: 1.15;
  }

  .contact-block { position: absolute; left: 195px; top: 34px; right: 14px; color: var(--ink); }
  .person-name { font-size: 20px; font-weight: 800; color: var(--brand-green); letter-spacing: 0.4px; line-height: 1; }
  .person-role { font-size: 11px; font-weight: 500; margin-top: 2px; }
  .back-company {
    font-size: 17px; font-weight: 600; color: var(--brand-green);
    margin-top: 16px; margin-bottom: 18px; white-space: nowrap;
  }
  .contact-list { list-style: none; }
  .contact-list li {
    display: flex; align-items: center; gap: 6px;
    font-size: 11px; font-weight: 500; height: 16.5px;
  }
  .contact-list svg { width: 10px; height: 10px; fill: var(--ink); flex: none; }
  .service-area { font-size: 11px; font-weight: 500; margin-top: 7px; }
</style>
</head>
<body>
<main class="canvas">
  <section class="card card-front" aria-label="Business card front">
    <p class="front-name">Crestline Lending Group</p>
    <p class="front-web">www.crestlinelending.com</p>
    <p class="front-services">TITLE LOANS | PERSONAL LOANS | TAX SERVICES</p>
  </section>

  <section class="card card-back" aria-label="Business card back">
    <div class="referral">
      <p class="referral-title">REFER A FRIEND</p>
      <p class="referral-sub">GET UP TO</p>
      <p class="referral-amount">$100</p>
    </div>
    <p class="back-mark">Crestline Lending Group</p>

    <div class="contact-block">
      <p class="person-name">MARIA SANTOS</p>
      <p class="person-role">Branch Manager</p>
      <p class="back-company">Crestline Lending Group</p>
      <ul class="contact-list">
        <li>
          <svg viewBox="0 0 24 24" aria-hidden="true"><path d="M6.6 10.8c1.4 2.8 3.8 5.1 6.6 6.6l2.2-2.2c.3-.3.7-.4 1-.2 1.1.4 2.3.6 3.6.6.6 0 1 .4 1 1V20c0 .6-.4 1-1 1C10.6 21 3 13.4 3 4c0-.6.4-1 1-1h3.5c.6 0 1 .4 1 1 0 1.3.2 2.5.6 3.6.1.3 0 .7-.2 1l-2.3 2.2z"/></svg>
          (505)555-0148
        </li>
        <li>
          <svg viewBox="0 0 24 24" aria-hidden="true"><path d="M2 5h20v14H2V5zm2 2v.5l8 5 8-5V7H4zm16 2.8-8 5-8-5V17h16V9.8z"/></svg>
          hello@crestlinelending.com
        </li>
        <li>
          <svg viewBox="0 0 24 24" aria-hidden="true"><path d="M12 2a10 10 0 1 0 0 20 10 10 0 0 0 0-20zm6.9 6h-3a15 15 0 0 0-1.3-3.9A8 8 0 0 1 18.9 8zM12 4c.8 1.2 1.5 2.5 1.9 4h-3.8c.4-1.5 1.1-2.8 1.9-4zM4.3 14a8 8 0 0 1 0-4h3.4a16 16 0 0 0 0 4H4.3zm.8 2h3a15 15 0 0 0 1.3 3.9A8 8 0 0 1 5.1 16zm3-8h-3a8 8 0 0 1 4.3-3.9C8.8 5.3 8.4 6.6 8.1 8zM12 20c-.8-1.2-1.5-2.5-1.9-4h3.8c-.4 1.5-1.1 2.8-1.9 4zm2.3-6H9.7a14 14 0 0 1 0-4h4.6a14 14 0 0 1 0 4zm.3 5.9c.6-1.2 1-2.5 1.3-3.9h3a8 8 0 0 1-4.3 3.9zm1.7-5.9a16 16 0 0 0 0-4h3.4a8 8 0 0 1 0 4h-3.4z"/></svg>
          www.crestlinelending.com
        </li>
      </ul>
      <p class="service-area">New Mexico, Texas, and Oklahoma.</p>
    </div>
  </section>
</main>
</body>
</html>
```